Save The Date- Vintage Hawaiian postcard theme

I'm looking for a custom design for the Save the Date for my wedding. I'm getting married in Maui, Hawaii in May, and I'd like a Save the Date that appears like a vintage Hawaiian postcard. I'd also like for it to say:Save the DateKayvon and Greta are getting marriedMay 10, 2020Maui, Hawaii

```html
<!DOCTYPE html>
<html lang="en">
<head>
<meta charset="utf-8">
<title>Save the Date – Tobias and Greta</title>
<link rel="stylesheet" href="https://fonts.googleapis.com/css2?family=Montserrat:wght@200;800&display=swap">
<style>
  :root {
    --page: #ffffff;
    --ink: #111111;
    --sky: #7cc4e4;
    --ocean: #3aa5c9;
    --sand: #f1e3c6;
    --lagoon: #8fd3cf;
    --palm: #8fae5a;
    --card-edge: #ffffff;
  }
  html, body {
    margin: 0;
    width: 1200px;
    height: 1200px;
    overflow: hidden;
    background: var(--page);
  }
  .canvas {
    position: relative;
    width: 1200px;
    height: 1200px;
  }
  .postcard {
    position: absolute;
    left: 60px;
    top: 240px;
    width: 1080px;
    height: 720px;
    background: var(--card-edge);
    padding: 8px;
    box-sizing: border-box;
    font-family: "Montserrat", sans-serif;
    color: var(--ink);
  }
  .beach-scene {
    position: absolute;
    inset: 8px;
    background:
      linear-gradient(180deg,
        var(--sky) 0%,
        var(--ocean) 18%,
        var(--sand) 30%,
        var(--sand) 44%,
        var(--lagoon) 52%,
        var(--lagoon) 72%,
        var(--palm) 88%,
        var(--sand) 100%);
  }
  .headline {
    position: absolute;
    left: 380px;
    top: 120px;
    margin: 0;
    font-weight: 200;
    font-size: 92px;
    letter-spacing: -1px;
    line-height: 1;
  }
  .heart-icon {
    position: absolute;
    left: 560px;
    top: 232px;
    width: 60px;
    height: 52px;
  }
  .couple-names {
    position: absolute;
    left: 340px;
    top: 300px;
    width: 520px;
    text-align: center;
    margin: 0;
    font-weight: 800;
    font-size: 50px;
    line-height: 1;
  }
  .announcement {
    position: absolute;
    left: 300px;
    top: 362px;
    width: 600px;
    text-align: center;
    margin: 0;
    font-weight: 200;
    font-size: 52px;
    line-height: 1;
  }
  .wedding-date,
  .wedding-place {
    position: absolute;
    margin: 0;
    font-weight: 800;
    font-size: 38px;
    line-height: 1;
  }
  .wedding-date { left: 120px; top: 470px; }
  .wedding-place { left: 700px; top: 560px; }
  .couple-portrait {
    position: absolute;
    left: 460px;
    top: 460px;
    width: 200px;
    height: 150px;
    border-radius: 12px;
    background: rgba(143, 211, 207, 0.75);
  }
</style>
</head>
<body>
  <main class="canvas">
    <article class="postcard">
      <div class="beach-scene" role="img" aria-label="Vintage halftone photograph of a curved Hawaiian beach with turquoise lagoon and palm trees"></div>

      <h1 class="headline">Save the date</h1>

      <svg class="heart-icon" viewBox="0 0 60 52" role="img" aria-label="Heart with arrow">
        <path d="M30 46 L10 26 A10 10 0 0 1 30 14 A10 10 0 0 1 50 26 Z" fill="none" stroke="#111" stroke-width="3" stroke-linejoin="round"/>
        <line x1="4" y1="46" x2="56" y2="6" stroke="#111" stroke-width="3"/>
        <path d="M56 6 L46 8 M56 6 L54 16" stroke="#111" stroke-width="3" fill="none"/>
      </svg>

      <p class="couple-names">Tobias and Greta</p>
      <p class="announcement">are getting married</p>

      <p class="wedding-date">May 10, 2020</p>
      <div class="couple-portrait" role="img" aria-label="Line illustration of the bride and groom"></div>
      <p class="wedding-place">Maui, Hawaii</p>
    </article>
  </main>
</body>
</html>
```